Paper Orchards (instructional dating book)

Title: Paper Orchards
Subtitle: Ways to charm a stranger across any crowded room
Author: R.J. Pollard
I'm seeking the title to be central with the subtitle underneath and the author slightly lower and to the left. Perhaps a border or two around the font. I thought the background could look aged (off color and old textured paper) and the background slightly punched into the texture like a typewriter has been used. I imagine it something like an old Fenwright playbook or 1940s morse code manual. Many thanks!

Target Market(s)

18 to 45 year old single people

Industry/Entity Type

Dating

Font styles to use
Serif

Requirements
Must have
• Text with border or two
Nice to have
• Traditional feel. The book is instructional.
Should not have
• Too much color or flair

```html
<!DOCTYPE html>
<html lang="en">
<head>
<meta charset="utf-8">
<title>Paper Orchards — R.J. Pollard</title>
<link rel="stylesheet" href="https://fonts.googleapis.com/css2?family=PT+Serif:wght@400&display=swap">
<style>
  :root {
    --paper-light: #f1dcae;
    --paper-mid: #e4bf83;
    --paper-warm: #d08a45;
    --paper-burnt: #a84616;
    --paper-edge: #6e240a;
    --rule: #b07a3c;
    --ink: #111008;
  }
  html, body {
    margin: 0;
    padding: 0;
    width: 834px;
    height: 1200px;
    overflow: hidden;
    background: var(--paper-edge);
  }
  .cover {
    position: relative;
    width: 834px;
    height: 1200px;
    overflow: hidden;
    font-family: "PT Serif", Georgia, serif;
    color: var(--ink);
  }
  .aged-paper {
    position: absolute;
    inset: 0;
    background:
      radial-gradient(ellipse 62% 58% at 50% 48%, var(--paper-light) 0%, var(--paper-mid) 55%, var(--paper-warm) 80%, var(--paper-burnt) 94%, var(--paper-edge) 100%);
  }
  .frame {
    position: absolute;
    inset: 0;
  }
  .title {
    position: absolute;
    left: 0;
    right: 0;
    margin: 0;
    text-align: center;
    font-weight: 400;
    line-height: 1;
  }
  .title-line-one {
    top: 218px;
    font-size: 196px;
    letter-spacing: 2px;
  }
  .title-line-two {
    top: 395px;
    font-size: 124px;
    letter-spacing: 1px;
  }
  .subtitle {
    position: absolute;
    left: 0;
    right: 0;
    top: 556px;
    margin: 0;
    text-align: center;
    font-size: 31px;
    line-height: 52px;
    text-transform: uppercase;
    font-weight: 400;
  }
  .author {
    position: absolute;
    left: 0;
    right: 16px;
    top: 826px;
    margin: 0;
    text-align: center;
    font-size: 68px;
    font-weight: 400;
    line-height: 1;
  }
</style>
</head>
<body>
<main class="cover">
  <div class="aged-paper" role="img" aria-label="Aged, stained parchment paper texture darkening to burnt orange at the edges"></div>

  <svg class="frame" width="834" height="1200" viewBox="0 0 834 1200" aria-hidden="true">
    <g fill="none" stroke="var(--rule)" stroke-width="2.5">
      <rect x="34" y="36" width="766" height="1132"/>
      <rect x="42" y="44" width="750" height="1116" stroke-width="1.5"/>
      <circle cx="60" cy="180" r="22"/>
      <circle cx="778" cy="180" r="22"/>
      <circle cx="60" cy="692" r="22"/>
      <circle cx="778" cy="692" r="22"/>
      <line x1="82" y1="180" x2="756" y2="180"/>
      <line x1="82" y1="692" x2="756" y2="692"/>
      <line x1="66" y1="202" x2="66" y2="670"/>
      <line x1="772" y1="202" x2="772" y2="670"/>
      <line x1="66" y1="714" x2="66" y2="1140"/>
      <line x1="772" y1="714" x2="772" y2="1140"/>
    </g>
  </svg>

  <h1 class="title title-line-one">PAPER</h1>
  <h1 class="title title-line-two">ORCHARDS</h1>
  <p class="subtitle">Ways to charm a stranger<br>across any crowded room</p>
  <p class="author">R.J. POLLARD</p>
</main>
</body>
</html>
```